Quillstone (real estate analytics tool) - Pavlora and Trembit Cover Page

We are a newly launched SaaS startup which specialises in market analytics for commercial, office and retail property sector: https://quillstone.com.au/
We need two images designed to serve as cover pages for Pavlora and Trembit business pages. The images should be same/similar, however adjusted to fit the cover image specifications of each platform (Pavlora: 1128 (w) x 191 (h) pixels https://www.pavlora.net/help/pavlora/answer/a563309/image-specifications-for-your-pavlora-pages-and-career-pages AND Trembit 1:8 aspect ration https://www.trembit.net/help/125379114252045)
The design should communicate analytics / analysis / people working on computers / perhaps with some playful aspects. The design should utilise our primary green colour (#1c7d39).
The attached screenshot shows the first attempt which we DO NOT like. It has no flow, it feels broken, the way the profile picture overlays the cover image is not great and feels broken.
Real Estate
- Caviar Dreams, Comfortaa

```html
<!DOCTYPE html>
<html lang="en">
<head>
<meta charset="utf-8">
<title>Quillstone – Cover</title>
<link href="https://fonts.googleapis.com/css2?family=Comfortaa:wght@400;600;700&family=Inter:wght@400;500;600;700&display=swap" rel="stylesheet">
<style>
  :root{
    --lime:#5fe41c;
    --lime-soft:#c9f2b0;
    --green-bg:#8fdc7a;
    --green-deep:#1c7d39;
    --ink:#333a3a;
    --muted:#8a9193;
    --line:#e6e9ea;
    --white:#ffffff;
    --bar-teal:#6fd0c6;
    --bar-blue:#7fa6e8;
    --bar-violet:#8d7be0;
    --bar-pink:#f39bb0;
    --bar-orange:#f6a35c;
    --bar-purple:#c195f0;
  }
  *{margin:0;padding:0;box-sizing:border-box}
  html,body{width:1200px;height:203px;overflow:hidden;background:var(--white)}
  .cover{position:relative;width:1200px;height:203px;overflow:hidden;font-family:"Inter",sans-serif}
  .cityscape{position:absolute;left:560px;top:0;width:640px;height:203px;
    background:linear-gradient(100deg,#cdeec0 0%,var(--green-bg) 45%,#a8e495 75%,#d6f3cb 100%)}
  .corner-tint{position:absolute;left:0;bottom:0;width:220px;height:60px;
    background:radial-gradient(ellipse at 0% 100%,#cfeec4 0%,rgba(255,255,255,0) 70%)}
  .white-shape{position:absolute;left:0;top:0}
  .headline{position:absolute;left:90px;top:52px;font-family:"Comfortaa",sans-serif;font-weight:600;font-size:30px;line-height:38px;color:var(--ink);letter-spacing:-.2px}
  .headline .accent{display:block;color:var(--lime)}
  .dot{position:absolute;width:9px;height:9px;border-radius:50%;background:var(--lime)}
  .app{position:absolute;left:798px;top:4px;width:420px;height:210px;background:var(--white);border-radius:6px 0 0 0;box-shadow:0 4px 18px rgba(0,0,0,.15);font-size:5px;color:var(--ink)}
  .sidebar{position:absolute;left:0;top:0;width:52px;height:100%;border-right:1px solid var(--line);padding:6px 5px}
  .brand{display:flex;align-items:center;gap:3px;font-size:6px;font-weight:600;color:var(--green-deep)}
  .brand i{width:5px;height:5px;background:var(--green-deep);border-radius:50%;display:block}
  .nav{margin-top:12px;display:flex;flex-direction:column;gap:6px;color:var(--muted)}
  .nav span.active{color:var(--green-deep);font-weight:600}
  .user{position:absolute;right:26px;top:8px;font-size:5px;color:var(--muted);display:flex;gap:3px;align-items:center}
  .user i{width:9px;height:9px;border-radius:50%;background:#d9dcdc;display:block}
  .search{position:absolute;left:58px;top:18px;width:290px;height:96px;border:1px solid var(--line);border-radius:4px;padding:6px 8px}
  .search h2{font-size:10px;font-weight:700;margin-bottom:7px}
  .field{position:absolute;font-size:4.5px;color:var(--muted)}
  .field b{display:block;margin-top:2px;height:9px;border:1px solid var(--line);border-radius:2px;padding:1px 3px;font-weight:400;color:var(--ink);font-size:4.5px}
  .btn{position:absolute;height:10px;border-radius:2px;font-size:4.5px;display:flex;align-items:center;justify-content:center;color:var(--white)}
  .btn.map{background:#3d4446}
  .btn.go{background:var(--green-deep)}
  .results{position:absolute;left:58px;top:122px;width:340px;font-size:4.5px}
  .results .title{color:var(--muted);margin-bottom:4px}
  .row{display:flex;gap:14px;padding:3px 0;border-top:1px solid var(--line)}
  .row span:first-child{width:70px}
  .row em{display:block;width:26px;height:3px;margin-top:1px;background:#e3e6e7;border-radius:2px}
  .chart-card{position:absolute;background:var(--white);border:2px solid var(--lime);border-radius:5px;box-shadow:0 4px 14px rgba(0,0,0,.18);padding:5px 7px}
  .chart-card h3{font-size:7.5px;font-weight:700;color:var(--ink)}
  .sector{left:727px;top:44px;width:128px;height:93px}
  .size{left:598px;top:136px;width:196px;height:80px}
</style>
</head>
<body>
<div class="cover">
  <div class="cityscape" role="img" aria-label="Green-tinted city skyline with office towers"></div>
  <svg class="white-shape" width="1200" height="203" viewBox="0 0 1200 203" aria-hidden="true">
    <path d="M0 0 H628 C610 60 640 150 700 203 H0 Z" fill="#ffffff"/>
  </svg>
  <div class="corner-tint"></div>

  <h1 class="headline">Analytics and Insights Tool for the<span class="accent">Commercial Property Market</span></h1>

  <span class="dot" style="left:715px;top:162px"></span>
  <span class="dot" style="left:654px;top:118px;width:7px;height:7px"></span>
  <span class="dot" style="left:1180px;top:56px"></span>
  <span class="dot" style="left:1134px;top:152px;width:7px;height:7px"></span>

  <div class="app">
    <aside class="sidebar">
      <div class="brand"><i></i>Quillstone</div>
      <nav class="nav"><span>Dashboard</span><span class="active">Listings</span><span>Reports</span></nav>
    </aside>
    <div class="user">Sam Miller<i></i></div>
    <section class="search">
      <h2>Quick Search</h2>
      <div class="field" style="left:8px;top:24px;width:130px">Suburb<b>Melbourne VIC 3000</b></div>
      <div class="field" style="left:150px;top:24px;width:130px">Property type<b>Office premises</b></div>
      <div class="field" style="left:8px;top:46px;width:60px">Floor area<b>50</b></div>
      <div class="field" style="left:76px;top:46px;width:62px">Price per annum<b>$120k</b></div>
      <div class="field" style="left:150px;top:46px;width:130px">Include leased<b>Last 3 months</b></div>
      <div class="field" style="left:8px;top:72px">More filters</div>
      <div class="btn map" style="left:150px;top:66px;width:60px">Show on map</div>
      <div class="btn go" style="left:216px;top:76px;width:64px">Show 128 results</div>
    </section>
    <section class="results">
      <div class="title">Recent searches</div>
      <div class="row"><span>12 Collins St</span><em></em><em></em><em></em></div>
      <div class="row"><span>88 King St</span><em></em><em></em><em></em></div>
      <div class="row"><span>5 Queen St</span><em></em><em></em><em></em></div>
      <div class="row"><span>40 Spencer St</span><em></em><em></em><em></em></div>
    </section>
  </div>

  <div class="chart-card sector">
    <h3>Listings per Industry Sector</h3>
    <svg width="114" height="72" viewBox="0 0 114 72" font-family="Inter, sans-serif" font-size="3.5" fill="#8a9193">
      <g stroke="#eef0f0" stroke-width=".5"><line x1="10" y1="12" x2="112" y2="12"/><line x1="10" y1="28" x2="112" y2="28"/><line x1="10" y1="44" x2="112" y2="44"/><line x1="10" y1="60" x2="112" y2="60"/></g>
      <text x="0" y="13">400</text><text x="0" y="29">300</text><text x="0" y="45">200</text><text x="0" y="61">100</text>
      <rect x="14" y="26" width="11" height="36" rx="2" fill="var(--bar-teal)"/>
      <rect x="30" y="22" width="11" height="40" rx="2" fill="var(--bar-blue)"/>
      <rect x="46" y="14" width="11" height="48" rx="2" fill="var(--bar-violet)"/>
      <rect x="62" y="54" width="11" height="8" rx="2" fill="var(--bar-pink)"/>
      <rect x="78" y="34" width="11" height="28" rx="2" fill="var(--bar-orange)"/>
      <rect x="94" y="42" width="11" height="20" rx="2" fill="var(--bar-purple)"/>
      <rect x="42" y="2" width="20" height="8" rx="2" fill="#3d4446"/>
      <text x="52" y="7.3" text-anchor="middle" fill="#fff">375 sites</text>
      <text x="14" y="68">Retail</text><text x="30" y="68">Office</text><text x="45" y="68">Industr.</text><text x="61" y="68">Parking</text><text x="78" y="68">Hotels</text><text x="93" y="68">Medical</text>
    </svg>
  </div>

  <div class="chart-card size">
    <h3>Listings per Size Segment (m²)</h3>
    <svg width="180" height="62" viewBox="0 0 180 62" font-family="Inter, sans-serif" font-size="3.5" fill="#8a9193">
      <g stroke="#eef0f0" stroke-width=".5"><line x1="12" y1="14" x2="178" y2="14"/><line x1="12" y1="30" x2="178" y2="30"/><line x1="12" y1="46" x2="178" y2="46"/></g>
      <text x="0" y="15">300</text><text x="0" y="31">200</text><text x="0" y="47">100</text>
      <rect x="18" y="24" width="16" height="40" rx="2" fill="var(--bar-violet)"/>
      <rect x="48" y="14" width="16" height="50" rx="2" fill="var(--bar-violet)"/>
      <rect x="78" y="32" width="16" height="32" rx="2" fill="var(--bar-violet)"/>
      <rect x="108" y="44" width="16" height="20" rx="2" fill="var(--bar-violet)"/>
      <rect x="138" y="52" width="16" height="12" rx="2" fill="var(--bar-violet)"/>
      <rect x="46" y="2" width="20" height="8" rx="2" fill="#3d4446"/>
      <text x="56" y="7.3" text-anchor="middle" fill="#fff">233 sites</text>
    </svg>
  </div>
</div>
</body>
</html>
```